Super Greens Label for Supplement Bottle

We want to design a front label for a health supplement bottle. The product is called Meadow Twist Chews™. This will be a new product so there is no current website for the product. The focus is on supergreens that taste great and deliver support for energy, digestion, and immune defense.
We want it to be modern, vibrant and appealing.
Bottle size: standard size supplement CLEAR bottle size, with white child resistant cap and the label panel dimensions are 3” x 7”. The label should be primarily white and green, with a touch of red; (see color palettes)/it can also ONLY be white and green. See samples attached.
We are only focused on the front of the bottle design, not on the back, but leave space for the supplement panel and other text on the back.
So the text for the front of the bottle is:
RT Balden's
Meadow Twist Chews™
Super Greens Blend for:
Energy, Digestion, and Immune Support*
60 Gummies | Dietary Supplement
Raspberry Flavor Gummies
Off to side of the label:
Non-GMO
Vegan Friendly
Plant-Based
Gelatin Free
Colors
Designer to choose colors to be used in the design.

```html
<!DOCTYPE html>
<html lang="en">
<head>
<meta charset="utf-8">
<title>Meadow Twist Chews™ – Front Label</title>
<link href="https://fonts.googleapis.com/css2?family=Poppins:wght@300;400;500;600;700&display=swap" rel="stylesheet">
<style>
  :root{
    --page:#eef0ee;
    --label:#ffffff;
    --panel:#f2f2f2;
    --green-dark:#1f6f2a;
    --green:#3d9b30;
    --green-mid:#6cbf4a;
    --green-light:#a6dc7c;
    --badge:#6cc46a;
    --ink:#3a3a3a;
    --ink-soft:#7a7a7a;
    --rule:#4a4a4a;
    --berry:#d8344f;
    --berry-light:#ea8296;
    --leaf:#b9e07a;
  }
  *{margin:0;padding:0;box-sizing:border-box;}
  html,body{width:1200px;height:1180px;overflow:hidden;}
  body{background:var(--page);font-family:"Poppins",sans-serif;position:relative;}

  .label{
    position:absolute;left:190px;top:29px;width:820px;height:1122px;
    background:var(--label);overflow:hidden;
    box-shadow:0 2px 10px rgba(0,0,0,.08);
  }
  .label-corner{position:absolute;left:0;top:0;}
  .content-panel{
    position:absolute;left:20px;top:170px;right:0;bottom:117px;
    background:linear-gradient(180deg,var(--label) 0%,var(--panel) 100%);
    border-top-left-radius:62px;
  }
  .brand-line{
    position:absolute;left:66px;top:200px;font-size:30px;font-weight:600;
    color:var(--ink);letter-spacing:.5px;white-space:nowrap;
  }
  .product-name{
    position:absolute;left:62px;font-weight:700;font-size:120px;line-height:120px;
    letter-spacing:-3px;color:var(--green);white-space:nowrap;
  }
  .product-name sup{font-size:40px;vertical-align:top;position:relative;top:14px;letter-spacing:0;}
  .name-1{top:250px;}
  .name-2{top:380px;}
  .name-3{top:490px;}

  .blend-heading{
    position:absolute;left:64px;top:636px;font-size:42px;font-weight:500;color:var(--ink-soft);
    letter-spacing:-.5px;white-space:nowrap;
  }
  .blend-heading strong{font-weight:600;color:var(--ink);}
  .benefits{
    position:absolute;left:64px;top:700px;font-size:38px;font-weight:400;line-height:52px;
    color:var(--ink-soft);letter-spacing:-.3px;
  }
  .divider{position:absolute;left:62px;top:905px;width:520px;height:3px;background:var(--rule);}
  .count-line{
    position:absolute;left:62px;top:936px;font-size:31px;font-weight:500;color:var(--ink-soft);
    letter-spacing:.2px;white-space:nowrap;
  }
  .count-line strong{font-weight:600;color:var(--ink);}

  .flavor-band{
    position:absolute;left:0;right:0;top:1004px;height:118px;
    background:linear-gradient(90deg,var(--berry) 0%,var(--berry-light) 100%);
  }
  .flavor-band span{
    position:absolute;left:78px;top:30px;color:#fff;font-size:42px;font-weight:600;letter-spacing:-.3px;
  }

  .raspberry-side{
    position:absolute;left:-30px;top:850px;width:80px;height:185px;border-radius:40px;
    background:radial-gradient(circle at 60% 40%,var(--berry-light),var(--berry));
  }
  .raspberry-corner{
    position:absolute;left:665px;top:790px;width:155px;height:214px;
    border-top-left-radius:90px 110px;border-bottom-left-radius:60px;
    background:radial-gradient(circle at 30% 20%,var(--leaf) 0%,var(--leaf) 26%,rgba(185,224,122,0) 44%),
               radial-gradient(circle at 66% 64%,var(--berry-light) 0%,var(--berry) 48%,rgba(216,52,79,0) 76%);
  }

  .badges{position:absolute;left:681px;top:200px;width:100px;}
  .badge{position:absolute;left:0;width:100px;text-align:center;}
  .badge svg{display:block;margin:0 auto;}
  .badge-text{
    display:block;margin-top:8px;font-size:17px;font-weight:300;line-height:24px;
    color:var(--ink);letter-spacing:.3px;white-space:nowrap;
  }
  .badge-gmo{top:0;}
  .badge-vegan{top:140px;}
  .badge-gelatin{top:280px;}
  .badge-plant{top:420px;}
</style>
</head>
<body>
  <main class="label">
    <svg class="label-corner" width="820" height="900" viewBox="0 0 820 900" role="img" aria-label="Radiating green leaf stripes decoration">
      <defs>
        <linearGradient id="leafFill" x1="0" y1="0" x2="1" y2="0.3">
          <stop offset="0" stop-color="#3fa84a"/>
          <stop offset="0.5" stop-color="#8fd36a"/>
          <stop offset="1" stop-color="#1f6f2a"/>
        </linearGradient>
        <linearGradient id="stripFill" x1="0" y1="0" x2="0" y2="1">
          <stop offset="0" stop-color="#3fa84a"/>
          <stop offset="1" stop-color="#8fd36a"/>
        </linearGradient>
      </defs>
      <path d="M0 0 H470 C440 95 360 165 250 172 L0 172 Z" fill="url(#leafFill)"/>
      <rect x="0" y="160" width="24" height="700" fill="url(#stripFill)"/>
    </svg>

    <div class="content-panel"></div>

    <div class="raspberry-side" role="img" aria-label="Raspberry illustration"></div>
    <div class="raspberry-corner" role="img" aria-label="Raspberry with green leaf illustration"></div>

    <p class="brand-line">RT Balden's</p>
    <h1>
      <span class="product-name name-1">Meadow</span>
      <span class="product-name name-2">Twist</span>
      <span class="product-name name-3">Chews<sup>™</sup></span>
    </h1>

    <p class="blend-heading">Super Greens <strong>Blend for:</strong></p>
    <p class="benefits">Energy, Digestion,<br>and Immune Support.*</p>

    <div class="divider"></div>
    <p class="count-line">60 GUMMIES | <strong>DIETARY SUPPLEMENT</strong></p>

    <div class="flavor-band"><span>Raspberry Flavor Gummies</span></div>

    <div class="badges">
      <div class="badge badge-gmo">
        <svg width="68" height="68" viewBox="0 0 68 68" aria-hidden="true">
          <circle cx="34" cy="34" r="32" fill="none" stroke="var(--badge)" stroke-width="2.5"/>
          <path d="M29 24 V32 L22 46 H40 L35 32 V24 Z" fill="var(--badge)"/>
          <path d="M34 22 C30 14 26 15 27 19 M34 22 C38 14 42 15 41 19" stroke="var(--badge)" stroke-width="2.5" fill="none"/>
          <circle cx="43" cy="43" r="7" fill="#fff" stroke="var(--badge)" stroke-width="2"/>
          <path d="M40 40 L46 46 M46 40 L40 46" stroke="var(--badge)" stroke-width="2"/>
        </svg>
        <span class="badge-text">NON-GMO</span>
      </div>
      <div class="badge badge-vegan">
        <svg width="68" height="68" viewBox="0 0 68 68" aria-hidden="true">
          <circle cx="34" cy="34" r="32" fill="none" stroke="var(--badge)" stroke-width="2.5"/>
          <path d="M24 44 C20 30 30 20 46 20 C47 36 38 45 24 44 Z" fill="var(--badge)"/>
          <path d="M22 48 L40 28" stroke="#fff" stroke-width="2" fill="none"/>
        </svg>
        <span class="badge-text">VEGAN<br>FRIENDLY</span>
      </div>
      <div class="badge badge-gelatin">
        <svg width="68" height="68" viewBox="0 0 68 68" aria-hidden="true">
          <circle cx="34" cy="34" r="32" fill="none" stroke="var(--badge)" stroke-width="2.5"/>
          <path d="M24 40 L26 24 C30 20 38 20 42 24 L44 40 Z" fill="var(--badge)"/>
          <path d="M30 26 V38 M34 25 V38 M38 26 V38" stroke="#fff" stroke-width="2"/>
          <ellipse cx="34" cy="43" rx="16" ry="4" fill="var(--badge)"/>
        </svg>
        <span class="badge-text">GELATIN<br>FREE</span>
      </div>
      <div class="badge badge-plant">
        <svg width="68" height="68" viewBox="0 0 68 68" aria-hidden="true">
          <circle cx="34" cy="34" r="32" fill="none" stroke="var(--badge)" stroke-width="2.5"/>
          <path d="M33 46 C22 44 18 34 22 24 C30 26 35 34 33 46 Z" fill="var(--badge)"/>
          <path d="M35 46 C36 36 40 30 48 29 C49 38 44 45 35 46 Z" fill="var(--badge)"/>
        </svg>
        <span class="badge-text">PLANT<br>BASED</span>
      </div>
    </div>
  </main>
</body>
</html>
```